Corvin Pixel Studio KRT

Using supplied photoshop components and looking at www.corvinpixelstudio.com/brieflane (click on menu at upper right and click on web site development; observe the animation effects on the right). I need you to use the supplied components to create this animation. Please ask questions.
Finished Project to be supplied in photoshop layered files. Please use a standard font such as verdana, Arial, Helvetica, sans-serif.

Font styles to use
Sans Serif

```html
<!DOCTYPE html>
<html lang="en">
<head>
<meta charset="utf-8">
<title>Web Site Design and Development – Corvin Pixel Studio KRT</title>
<link rel="stylesheet" href="https://fonts.googleapis.com/css2?family=Arimo:wght@700&family=Noto+Sans:wght@400&display=swap">
<style>
  :root {
    --page-bg: #ffffff;
    --frame-gold: #f2b21c;
    --frame-orange: #f08a00;
    --body-ink: #111111;
    --headline-red: #d0121b;
    --brand-ink: #3a3a3a;
    --brand-dot: #f29a1f;
  }
  html, body {
    margin: 0;
    padding: 0;
    width: 1200px;
    height: 259px;
    overflow: hidden;
    background: var(--page-bg);
  }
  .banner {
    position: relative;
    box-sizing: border-box;
    width: 1200px;
    height: 259px;
    border: 2px solid var(--frame-gold);
    border-radius: 14px;
    box-shadow: inset 0 0 0 1px rgba(240, 138, 0, 0.25);
    background: var(--page-bg);
    overflow: hidden;
  }
  .copy {
    position: absolute;
    left: 29px;
    top: 24px;
    width: 640px;
    height: 210px;
    overflow: hidden;
    font-family: "Noto Sans", Verdana, sans-serif;
    color: var(--body-ink);
  }
  .copy__label {
    margin: 0 0 18px;
    font-size: 18px;
    line-height: 24px;
    font-weight: 400;
  }
  .copy__text {
    margin: 0;
    font-size: 17.2px;
    line-height: 22.6px;
    white-space: nowrap;
  }
  .feature {
    position: absolute;
    left: 660px;
    top: 0;
    width: 480px;
    height: 259px;
    text-align: center;
  }
  .feature__headline {
    position: absolute;
    left: 0;
    width: 100%;
    margin: 0;
    font-family: "Arimo", Arial, sans-serif;
    font-weight: 700;
    font-size: 35px;
    line-height: 40px;
    color: var(--headline-red);
  }
  .feature__headline--top { top: 22px; }
  .feature__headline--bottom { top: 192px; }
  .brand {
    position: absolute;
    left: 0;
    top: 108px;
    width: 100%;
    display: flex;
    align-items: center;
    justify-content: center;
    gap: 14px;
  }
  .brand__dot {
    width: 22px;
    height: 22px;
  }
  .brand__name {
    font-family: "Noto Sans", Verdana, sans-serif;
    font-weight: 400;
    font-size: 30px;
    letter-spacing: 1px;
    color: var(--brand-ink);
    line-height: 40px;
  }
</style>
</head>
<body>
  <main class="banner">
    <section class="copy">
      <h2 class="copy__label">Row 5 Column 1</h2>
      <p class="copy__text">Lorem ipsum dolor sit amet, ne sea vocent scripta abhorreant,<br>facilisi explicari mel ne, ut quo vide ridens. Mei ex quodsi<br>inciderint, quo ad quas deleniti definitionem, vis no wisi graecis<br>offendit. Ius ut everti detraxit expetenda, meis civibus<br>consectetuer ea usu. Ad qui option facilisis consequuntur, pro<br>omnis aliquip vulputate te. Solum affert expetenda eos te, et<br>vim sale iudico impetus, in appetere postulant ius. Alia nihil</p>
    </section>
    <section class="feature">
      <h1 class="feature__headline feature__headline--top">Web Site Design</h1>
      <div class="brand">
        <svg class="brand__dot" viewBox="0 0 22 22" aria-hidden="true">
          <circle cx="11" cy="11" r="11" fill="var(--brand-dot)"/>
        </svg>
        <span class="brand__name">Corvin Pixel Studio KRT</span>
      </div>
      <p class="feature__headline feature__headline--bottom">and Development</p>
    </section>
  </main>
</body>
</html>
```